Professional Single Page Website Design for Velloway Advisory

Velloway Advisory is a new business consultancy specializing in providing expert services to small businesses, primarily in the brick-and-mortar retail and food service sectors. We offer a range of services including franchise development and launch, due diligence, and construction management.

Currently, we have a basic website set up at www.vellowayadvisory.example, but we need a professional touch to enhance its design and functionality.

Project Requirements:
- Single Page Design: For now, we need a single page design that effectively showcases who we are, our services, and contact information.
- Future Expansion: The design should be flexible and scalable for future expansion to include additional pages like specific service offerings, about us, and a dedicated contact page.
- Design Aesthetic: We are looking for a modern yet professional design that aligns with our brand identity.
- Logo: We have a logo that we like, which was also sourced from Pixel Forum. The logo files are attached to this project brief.

Key Sections to Include:
- Hero Section: An engaging introduction to Velloway Advisory with a strong visual impact.
- About Us: A brief overview of who we are and our mission.
- Team: Section for the profiles of the two principals.
- Services: A clear and concise presentation of our services, including franchise development, due diligence, and construction management.
- Contact Information: Easy-to-find contact details, including a form for inquiries.
- Call to Action: Encouraging visitors to get in touch with us for consultations or further information.

Design Considerations:
- Ensure the design is responsive and mobile-friendly.
- Include high-quality images and icons that complement our services and industry.
- We do not need development services, this is only a design project.

```html
<!DOCTYPE html>
<html lang="en">
<head>
<meta charset="utf-8">
<title>Velloway Advisory</title>
<link href="https://fonts.googleapis.com/css2?family=Poppins:wght@300;400;500;600;700&display=swap" rel="stylesheet">
<style>
:root{
  --green:#93c9b0;
  --green-deep:#7fbb9f;
  --green-pale:#e7f2ed;
  --ink:#212b33;
  --ink-soft:#4a5258;
  --footer:#252f36;
  --white:#ffffff;
  --line:#d9e6e0;
}
*{box-sizing:border-box;margin:0;padding:0}
html,body{width:1200px;height:4323px;overflow:hidden}
body{font-family:'Poppins',sans-serif;color:var(--ink);background:var(--white);position:relative}
.abs{position:absolute}
/* header */
.site-header{position:absolute;top:0;left:0;width:1200px;height:154px;background:var(--white)}
.brand{position:absolute;left:75px;top:30px;display:flex;align-items:center;gap:14px}
.brand-dot{width:96px;height:96px;border-radius:50%;border:8px solid var(--green)}
.brand-name{font-size:30px;font-weight:600;color:var(--ink);line-height:1.05;width:180px}
.nav{position:absolute;top:74px;right:78px;display:flex;gap:36px;font-size:14px;color:var(--ink-soft)}
.nav a{color:inherit;text-decoration:none;padding-bottom:6px}
.nav a.active{color:var(--ink);border-bottom:2px solid var(--green)}
/* hero */
.hero{position:absolute;top:154px;left:0;width:1200px;height:697px;overflow:hidden}
.hero-photo{position:absolute;inset:0;background:linear-gradient(180deg,#6faec4 0%,#94c3cf 55%,#6f8fa0 100%)}
.hero-tower{position:absolute;left:873px;top:0;width:327px;height:697px;background:linear-gradient(180deg,#c9a194,#b98f82)}
.hero-diamond{position:absolute;left:140px;top:4px;width:486px;height:486px;border-radius:120px;transform:translate(0,0) rotate(45deg);transform-origin:center;background:rgba(235,244,246,.72)}
.hero-text{position:absolute;left:0;width:712px;text-align:center}
.hero h1{font-size:58px;font-weight:700;line-height:1}
.hero .sub{font-size:44px;font-weight:400;margin-top:8px}
.hero .tag{font-size:26px;margin-top:22px;font-weight:400}
.hero .tag b{font-weight:600;display:block}
.btn-dark{position:absolute;display:flex;align-items:center;background:var(--ink);color:var(--white);border-radius:30px;font-size:16px;font-weight:600;padding-left:18px}
.btn-mark{position:absolute;right:-4px;top:-2px;border-radius:50%;background:var(--green);display:flex;align-items:center;justify-content:center;border:3px solid var(--white)}
/* about */
.about{position:absolute;top:935px;left:0;width:1200px;height:572px;background:var(--green);overflow:hidden}
.sec-title{font-size:56px;font-weight:600;line-height:1}
.sec-sub{font-size:24px;display:flex;align-items:center;gap:14px}
.sec-sub .rule{height:2px;width:70px;background:var(--ink)}
.about p{font-size:13.5px;line-height:22.5px;color:var(--ink)}
.about-frame{position:absolute;left:676px;top:92px;width:420px;height:420px;border-radius:90px;transform:rotate(45deg);background:rgba(255,255,255,.35)}
.about-photo{position:absolute;left:690px;top:104px;width:395px;height:395px;border-radius:80px;transform:rotate(45deg);background:linear-gradient(160deg,#dfe7ec 0%,#b9a997 50%,#6c6a6b 100%)}
/* services */
.blob{position:absolute;background:var(--green-pale);border-radius:160px;transform:rotate(45deg)}
.center{position:absolute;left:0;width:1200px;text-align:center}
.center .sec-sub{justify-content:center;color:var(--green-deep)}
.center .sec-sub .rule{width:36px}
.card{position:absolute;background:var(--white);border-radius:10px;box-shadow:0 0 14px rgba(147,201,176,.45);text-align:center}
.card.featured{border:2px solid var(--ink);box-shadow:none}
.card-photo{position:absolute;left:10px;right:10px;top:10px;height:197px}
.card-icon{position:absolute;left:50%;margin-left:-38px;width:76px;height:76px;border-radius:22px;transform:rotate(45deg);background:var(--white);box-shadow:0 4px 10px rgba(0,0,0,.12);display:flex;align-items:center;justify-content:center}
.card-icon svg{transform:rotate(-45deg)}
.card h3{font-size:20px;font-weight:600}
.card p{font-size:13px;line-height:22px;color:var(--ink-soft)}
/* team */
.member{position:absolute;width:320px;height:448px;background:var(--white);border-radius:10px;box-shadow:0 0 12px rgba(0,0,0,.08)}
.member-photo{position:absolute;left:8px;top:8px;width:304px;height:233px}
.member h4{position:absolute;left:26px;top:270px;font-size:23px;font-weight:500}
.member .role{position:absolute;left:26px;top:302px;font-size:20px;color:var(--green-deep)}
.member .divider{position:absolute;left:26px;top:333px;width:190px;height:1px;background:#bbb}
.member .icons{position:absolute;left:215px;top:316px;display:flex;gap:8px}
.member .icons span{width:32px;height:32px;border-radius:9px;background:var(--ink);transform:rotate(45deg);display:flex;align-items:center;justify-content:center}
.member .icons svg{transform:rotate(-45deg)}
.member p{position:absolute;left:28px;top:360px;width:270px;font-size:13px;line-height:22px;color:var(--ink-soft)}
/* contact */
.field{position:absolute;background:var(--white);border:1px solid #e0e6e3;box-shadow:0 2px 8px rgba(0,0,0,.06);font-size:13px;color:#9aa0a3;padding:16px 20px}
.map{position:absolute;left:649px;top:3311px;width:420px;height:381px;border-radius:26px;background:linear-gradient(135deg,#eef1ec,#dfe8e4 60%,#d6e6f2);box-shadow:0 0 10px rgba(0,0,0,.08)}
.btn-green{position:absolute;left:120px;top:3745px;width:166px;height:58px;border-radius:30px;background:var(--green);color:var(--white);font-size:17px;font-weight:600;padding:18px 0 0 30px}
/* footer */
.footer{position:absolute;top:3846px;left:0;width:1200px;height:408px;background:var(--footer);color:var(--white)}
.footer h5{position:absolute;font-size:22px;font-weight:500}
.footer .uline{position:absolute;height:1px;background:#6f7a80}
.footer ul{position:absolute;list-style:none;font-size:13px;line-height:26.5px}
.footer ul li::before{content:"";display:inline-block;width:9px;height:9px;border:1.5px solid var(--green);transform:rotate(45deg);margin-right:10px}
.contact-row{position:absolute;display:flex;gap:16px;font-size:13px;line-height:16px}
.contact-row .dia{width:30px;height:30px;border:1.5px solid var(--white);border-radius:6px;transform:rotate(45deg);flex:none;margin-left:5px}
.socials{position:absolute;left:84px;top:288px;display:flex;gap:12px}
.socials span{width:34px;height:34px;border:1.5px solid var(--white);border-radius:6px;transform:rotate(45deg);display:flex;align-items:center;justify-content:center}
.socials span i{width:12px;height:12px;border-radius:50%;background:var(--white)}
.newsletter{position:absolute;left:887px;top:268px;width:210px;height:36px;border:1px solid var(--white);border-radius:20px;font-size:12px;padding:9px 16px}
.copyright{position:absolute;top:4254px;left:0;width:1200px;height:69px;background:var(--green);text-align:center;font-size:12px;padding-top:27px;color:var(--ink)}
</style>
</head>
<body>

<header class="site-header">
  <div class="brand"><div class="brand-dot"></div><div class="brand-name">Velloway Advisory</div></div>
  <nav class="nav">
    <a class="active" href="#">HOME</a><a href="#">WHO WE ARE</a><a href="#">OUR SERVICES</a><a href="#">TEAM</a><a href="#">CONTACT US</a>
  </nav>
</header>

<section class="hero">
  <div class="hero-photo" role="img" aria-label="City skyline of glass office towers under a blue sky"></div>
  <div class="hero-tower" role="img" aria-label="Close view of a residential high-rise facade with balconies"></div>
  <div class="hero-diamond"></div>
  <div class="hero-text" style="top:216px">
    <h1>Building Success</h1>
    <div class="sub">in Southern California</div>
    <div class="tag">Expertise at Every Step:<b>From Planning to Execution</b></div>
  </div>
  <div class="btn-dark" style="left:262px;top:477px;width:194px;height:59px">LEARN MORE
    <span class="btn-mark" style="width:60px;height:60px"><svg width="24" height="24" viewBox="0 0 24 24" fill="none" stroke="#fff" stroke-width="2.5"><path d="M5 12h14M13 6l6 6-6 6"/></svg></span>
  </div>
</section>

<section class="about">
  <div class="abs" style="left:98px;top:60px">
    <div class="sec-title">About Us</div>
    <div class="sec-sub" style="margin-top:6px">Who We Are <span class="rule"></span></div>
  </div>
  <p class="abs" style="left:101px;top:217px;width:460px">Welcome to Velloway Advisory, your trusted partner in navigating the complexities of the real estate and small business markets. Founded by industry veterans Daniel Reyes and Kevin Lau, we specialize in providing comprehensive services tailored to the unique needs of our clients. Whether you're a franchisee, a new restaurant owner, or a commercial real estate investor, our expertise in due diligence</p>
  <div class="btn-dark" style="left:101px;top:420px;width:192px;height:56px">READ MORE
    <span class="btn-mark" style="width:58px;height:58px"><svg width="22" height="22" viewBox="0 0 24 24" fill="none" stroke="#fff" stroke-width="2.5"><path d="M5 12h14M13 6l6 6-6 6"/></svg></span>
  </div>
  <div class="about-frame"></div>
  <div class="about-photo" role="img" aria-label="Downtown apartment buildings and rooftops"></div>
</section>

<div class="blob" style="left:870px;top:2100px;width:620px;height:620px"></div>
<div class="blob" style="left:-330px;top:3150px;width:520px;height:520px"></div>

<section>
  <div class="center" style="top:1636px">
    <div class="sec-title">Our Services</div>
    <div class="sec-sub" style="margin-top:8px">What We Do <span class="rule"></span></div>
  </div>
  <div class="center" style="top:1703px"><div class="sec-sub"><span class="rule"></span><span style="visibility:hidden">What We Do</span><span style="width:50px"></span></div></div>

  <div class="card" style="left:72px;top:1818px;width:324px;height:412px">
    <div class="card-photo" role="img" aria-label="Business handshake in front of a city view" style="background:linear-gradient(135deg,#f3ecd9,#b9b6ae 60%,#6f7072)"></div>
    <div class="card-icon" style="top:170px"><svg width="34" height="34" viewBox="0 0 24 24" fill="none" stroke="#333" stroke-width="1.4"><path d="M3 20h18M5 20V9l7-4 7 4v11M9 20v-5h6v5"/></svg></div>
    <h3 style="margin-top:276px">Franchise Development</h3>
    <p style="margin:14px 30px 0">Comprehensive franchise setup from evaluation to launch for scalable business growth.</p>
  </div>

  <div class="card featured" style="left:436px;top:1795px;width:322px;height:448px">
    <div class="card-photo" role="img" aria-label="Two colleagues reviewing charts at a desk" style="background:linear-gradient(135deg,#6b5a4f,#d8d4cf 55%,#c9d3df)"></div>
    <div class="card-icon" style="top:172px"><svg width="34" height="34" viewBox="0 0 24 24" fill="none" stroke="#333" stroke-width="1.4"><path d="M7 3h8l4 4v14H7z"/><path d="M10 11h6M10 15h6"/><circle cx="6" cy="8" r="3"/></svg></div>
    <h3 style="margin-top:276px">Due Diligence</h3>
    <p style="margin:14px 34px 0">Velloway offers comprehensive evaluations tailored to your business needs.</p>
    <svg class="abs" style="left:146px;top:387px" width="30" height="24" viewBox="0 0 30 24" fill="none" stroke="#333" stroke-width="1.6"><path d="M6 12h20M20 6l6 6-6 6"/><path d="M8 4l-6 8 6 8"/></svg>
  </div>

  <div class="card" style="left:795px;top:1818px;width:323px;height:412px">
    <div class="card-photo" role="img" aria-label="Team in hard hats reviewing construction plans" style="background:linear-gradient(135deg,#b7c3cf,#3f6aa8 55%,#e2e4e6)"></div>
    <div class="card-icon" style="top:170px"><svg width="34" height="34" viewBox="0 0 24 24" fill="none" stroke="#333" stroke-width="1.4"><path d="M7 3h8l4 4v14H7z"/><path d="M10 11h6M10 15h6"/><circle cx="6" cy="8" r="3"/></svg></div>
    <h3 style="margin-top:276px">Construction Management</h3>
    <p style="margin:14px 38px 0">Our Building &amp; Construction Management Services oversee every aspect of your construction</p>
  </div>
</section>

<section>
  <div class="center" style="top:2362px">
    <div class="sec-title">Our Team</div>
    <div class="sec-sub" style="margin-top:4px"><span class="rule"></span>Velloway Advisory<span class="rule"></span></div>
  </div>

  <article class="member" style="left:237px;top:2539px">
    <div class="member-photo" role="img" aria-label="Portrait of Daniel Reyes" style="background:linear-gradient(180deg,#a9c7e6,#c9c2b6 60%,#d9d4cc)"></div>
    <h4>Daniel Reyes</h4><div class="role">Principal</div><div class="divider"></div>
    <div class="icons"><span><svg width="14" height="14" viewBox="0 0 24 24" fill="#fff"><path d="M6 2l4 4-2 3a12 12 0 007 7l3-2 4 4-3 4C10 22 2 14 2 5z"/></svg></span><span><svg width="14" height="14" viewBox="0 0 24 24" fill="none" stroke="#fff" stroke-width="2"><rect x="3" y="5" width="18" height="14"/><path d="M3 5l9 8 9-8"/></svg></span></div>
    <p>Daniel Reyes brings almost 20 years of rich experience as a real estate...</p>
  </article>

  <article class="member" style="left:643px;top:2539px">
    <div class="member-photo" role="img" aria-label="Portrait of Kevin Lau" style="background:linear-gradient(180deg,#6d5a44,#8a7255 60%,#2a2c33)"></div>
    <h4>Kevin Lau</h4><div class="role">Principal</div><div class="divider"></div>
    <div class="icons"><span><svg width="14" height="14" viewBox="0 0 24 24" fill="#fff"><path d="M6 2l4 4-2 3a12 12 0 007 7l3-2 4 4-3 4C10 22 2 14 2 5z"/></svg></span><span><svg width="14" height="14" viewBox="0 0 24 24" fill="none" stroke="#fff" stroke-width="2"><rect x="3" y="5" width="18" height="14"/><path d="M3 5l9 8 9-8"/></svg></span></div>
    <p>Kevin Lau is a seasoned real estate expert with extensive experience in...</p>
  </article>
</section>

<section>
  <div class="abs" style="left:118px;top:3184px">
    <div class="sec-title">Contact Us</div>
    <div class="sec-sub" style="margin-top:4px;color:var(--green-deep)">Get In Touch <span class="rule" style="width:144px"></span></div>
  </div>
  <p class="abs" style="left:126px;top:3324px;width:480px;font-size:22px;line-height:31px;color:var(--ink)">Encouraging visitors to get in touch with us for consultations or further information.</p>
  <div class="field" style="left:117px;top:3440px;width:225px;height:48px">Name</div>
  <div class="field" style="left:360px;top:3440px;width:224px;height:48px">Phone</div>
  <div class="field" style="left:117px;top:3506px;width:467px;height:48px">Email Address</div>
  <div class="field" style="left:117px;top:3572px;width:467px;height:148px">Message</div>
  <div class="btn-green">SUBMIT
    <span class="btn-mark" style="width:62px;height:62px;right:-6px;top:-2px"><svg width="22" height="22" viewBox="0 0 24 24" fill="none" stroke="#fff" stroke-width="2.5"><path d="M5 12h14M13 6l6 6-6 6"/></svg></span>
  </div>
  <div class="map" role="img" aria-label="Street map showing the office location in Tustin"></div>
</section>

<footer class="footer">
  <div class="abs" style="left:121px;top:34px;width:100px;height:100px;border-radius:50%;border:9px solid var(--green)"></div>
  <div class="abs" style="left:72px;top:236px;width:200px;text-align:center;font-size:20px;font-weight:500">Velloway Advisory</div>
  <div class="socials"><span><i></i></span><span><i></i></span><span><i></i></span><span><i></i></span></div>

  <h5 style="left:364px;top:124px">Quik Links</h5>
  <div class="uline" style="left:364px;top:164px;width:120px"></div>
  <ul style="left:364px;top:184px"><li>Home</li><li>Who We Are</li><li>Our Services</li><li>Team</li><li>Contact Us</li></ul>

  <h5 style="left:594px;top:122px">Contact</h5>
  <div class="uline" style="left:594px;top:164px;width:200px"></div>
  <div class="contact-row" style="left:594px;top:188px"><span class="dia"></span><div>CALL US<br>0100 555 0142</div></div>
  <div class="contact-row" style="left:594px;top:236px"><span class="dia"></span><div>EMAIL US<br>hello@vellowayadvisory.example</div></div>
  <div class="contact-row" style="left:594px;top:284px"><span class="dia"></span><div>410 Harbor Park Dr Suite 200<br>Tustin, CA 92780</div></div>

  <h5 style="left:889px;top:124px">Our Newsletter</h5>
  <div class="uline" style="left:889px;top:164px;width:210px"></div>
  <p class="abs" style="left:895px;top:186px;width:220px;font-size:12.5px;line-height:17px">Get all the latest information on Special Discounts, Products and Offers.</p>
  <div class="newsletter">Enter Email Address
    <svg class="abs" style="right:6px;top:5px" width="24" height="24" viewBox="0 0 24 24" fill="none" stroke="#fff" stroke-width="1.5"><circle cx="12" cy="12" r="10"/><path d="M7 12h10M13 8l4 4-4 4"/></svg>
  </div>
</footer>
<div class="copyright">Copyright © 2024 All Rights Reserved By Velloway Advisory</div>

</body>
</html>
```